Kestrel Photography Business Card

I need a business card designed for a photography business based in Perth, Western Australia called Kestrel Photography.

We specialise in wedding, event photography and portrait photography.

The business card must borrow the style of the attached logo.

The hex codes for the colours in the logo are:
#ED1D85 - Pink
#89C23E - Green
#37282F - Black

The name on the card will be:
Name: Toviran
Phone: 0417395268
Website: www.kestrelphotography.com.au
Facebook: kestrelphotography

I am open and happy to accept creative concepts.

I’d like some space at the back for writing notes and appointment details.

```html
<!DOCTYPE html>
<html lang="en">
<head>
<meta charset="utf-8">
<title>Kestrel Photography – Business Card</title>
<link rel="stylesheet" href="https://fonts.googleapis.com/css2?family=Montserrat:wght@400;500;700&display=swap">
<style>
  :root {
    --pink: #ED1D85;
    --green: #89C23E;
    --black: #37282F;
    --white: #FFFFFF;
    --ink: #3A3A3A;
    --rule: #9A9A9A;
    --backdrop: #ECE9E4;
  }
  * { box-sizing: border-box; margin: 0; padding: 0; }
  html, body {
    width: 1200px; height: 720px; overflow: hidden;
    background: var(--backdrop);
    font-family: "Montserrat", sans-serif;
  }
  .sheet {
    width: 1200px; height: 720px;
    display: flex; align-items: center; justify-content: center; gap: 40px;
  }
  .card {
    position: relative;
    width: 540px; height: 324px;
    border-radius: 4px;
    overflow: hidden;
    box-shadow: 0 6px 18px rgba(0,0,0,0.18);
  }

  /* Front */
  .card--front { background: var(--white); }
  .card__swoosh { position: absolute; inset: 0; width: 100%; height: 100%; }
  .brand {
    position: absolute; left: 0; right: 0;
    display: flex; flex-direction: column; align-items: center;
  }
  .card--front .brand { top: 26px; left: 40px; right: auto; width: 340px; }
  .brand__mark {
    width: 54px; height: 54px; border-radius: 50%;
    background: var(--pink);
  }
  .brand__name {
    margin-top: 14px;
    font-size: 12px; font-weight: 400;
    letter-spacing: 0.55em; text-transform: uppercase;
    color: var(--black);
    white-space: nowrap;
  }
  .contact {
    position: absolute; left: 40px; top: 150px;
    list-style: none;
    font-size: 13px; color: var(--ink);
  }
  .contact__item { display: flex; align-items: center; gap: 8px; margin-bottom: 8px; }
  .contact__icon { width: 13px; height: 13px; flex: none; }
  .holder {
    position: absolute; right: 26px; top: 182px;
    font-size: 16px; font-weight: 700; letter-spacing: 0.03em;
    color: var(--pink); text-transform: uppercase;
  }

  /* Back */
  .card--back { background: var(--pink); }
  .card--back .brand { top: 26px; }
  .card--back .brand__mark { background: var(--white); width: 52px; height: 52px; }
  .card--back .brand__name { color: var(--white); margin-top: 10px; }
  .notes {
    position: absolute; left: 16px; right: 24px; top: 118px; height: 156px;
    background: var(--white);
    padding: 18px 18px 0 18px;
  }
  .notes__line { height: 22px; border-bottom: 1px dotted var(--rule); }
  .notes__line--labelled { display: flex; align-items: flex-end; gap: 6px; border-bottom: none; }
  .notes__label { font-size: 15px; font-weight: 500; color: var(--ink); line-height: 1; padding-bottom: 2px; }
  .notes__label + .notes__fill { flex: 1; border-bottom: 1px dotted var(--rule); height: 100%; }
  .web {
    position: absolute; left: 0; right: 0; bottom: 16px;
    text-align: center;
    font-size: 14px; letter-spacing: 0.14em; color: var(--white);
  }
</style>
</head>
<body>
<main class="sheet">

  <section class="card card--front" aria-label="Business card front">
    <svg class="card__swoosh" viewBox="0 0 540 324" preserveAspectRatio="none" aria-hidden="true">
      <path d="M540 128 C440 160 330 240 262 324 L540 324 Z" fill="var(--green)"/>
      <path d="M540 104 C430 140 320 230 236 324 L252 324 C330 236 440 150 540 120 Z" fill="var(--black)"/>
      <path d="M540 84 C470 100 430 116 400 132 C440 114 480 100 540 92 Z" fill="var(--pink)"/>
      <path d="M0 262 C60 300 140 298 200 290 C140 310 60 316 0 300 Z" fill="var(--pink)"/>
      <path d="M0 290 C80 318 150 312 210 300 L202 324 L0 324 Z" fill="var(--black)"/>
    </svg>

    <div class="brand">
      <span class="brand__mark"></span>
      <p class="brand__name">Kestrel Photography</p>
    </div>

    <ul class="contact">
      <li class="contact__item">
        <svg class="contact__icon" viewBox="0 0 14 14" aria-hidden="true">
          <circle cx="7" cy="7" r="6.3" fill="none" stroke="var(--green)" stroke-width="1.2"/>
          <path d="M4.6 3.8 L5.8 3.6 L6.4 5.3 L5.6 5.9 C6 7 6.9 7.9 8 8.3 L8.6 7.5 L10.2 8.1 L10.1 9.3 C7 9.8 4 6.8 4.6 3.8 Z" fill="var(--green)"/>
        </svg>
        <span>0417395268</span>
      </li>
      <li class="contact__item">
        <svg class="contact__icon" viewBox="0 0 14 14" aria-hidden="true">
          <rect x="0.5" y="0.5" width="13" height="13" rx="2" fill="var(--black)"/>
        </svg>
        <span>kestrelphotography</span>
      </li>
      <li class="contact__item">
        <svg class="contact__icon" viewBox="0 0 14 14" aria-hidden="true">
          <circle cx="7" cy="7" r="6.3" fill="none" stroke="var(--green)" stroke-width="1.2"/>
          <ellipse cx="7" cy="7" rx="2.6" ry="6.3" fill="none" stroke="var(--green)" stroke-width="1"/>
          <line x1="0.8" y1="7" x2="13.2" y2="7" stroke="var(--green)" stroke-width="1"/>
        </svg>
        <span>www.kestrelphotography.com.au</span>
      </li>
    </ul>

    <p class="holder">Toviran</p>
  </section>

  <section class="card card--back" aria-label="Business card back">
    <div class="brand">
      <span class="brand__mark"></span>
      <p class="brand__name">Kestrel Photography</p>
    </div>

    <div class="notes">
      <div class="notes__line"></div>
      <div class="notes__line"></div>
      <div class="notes__line notes__line--labelled">
        <span class="notes__label">notes:</span><span class="notes__fill"></span>
      </div>
      <div class="notes__line"></div>
      <div class="notes__line"></div>
      <div class="notes__line"></div>
    </div>

    <p class="web">www.kestrelphotography.com.au</p>
  </section>

</main>
</body>
</html>
```